Venbrook Finishes website

Epoxy Resin Flooring for home renovations and commercial property.
3 page website homepage, contact us and gallery with a link to Instagram.
Looking for someone to create a visually pleasing website for home transformation and design. I have attached some designs of completed work however I can send you many more. Use colour and don’t inspiration from the logo. If happy with stage one we will add a commercial page as a new project.

Target Market(s)

Homeowners that want to improve their home or rental property

Industry/Entity Type

Home improvements

Coding

Coded - Design and coding required

Number of Pages Required

3 page

Requirements
Must have
• Home Page, Contact Us page and showcase / gallery page
Nice to have
• I would like the colour theme to be taken from the logo, a clean finish with artistic usuals to get homeowners excited about their project

```html
<!DOCTYPE html>
<html lang="en">
<head>
<meta charset="utf-8">
<title>Venbrook Finishes – Epoxy Resin Flooring</title>
<link href="https://fonts.googleapis.com/css2?family=Montserrat:wght@400;500;600;700;800&display=swap" rel="stylesheet">
<style>
:root{
  --red:#ec1c24;
  --ink:#111;
  --text:#333;
  --grey-bg:#ededed;
  --header-bg:#f6f6f6;
  --field:#f4f4f4;
  --photo-dark:#4a4c4e;
  --photo-mid:#6b6d6f;
  --white:#fff;
}
*{margin:0;padding:0;box-sizing:border-box}
html,body{width:1200px;height:3968px;overflow:hidden}
body{font-family:'Montserrat',sans-serif;color:var(--text);background:var(--white);position:relative}
.abs{position:absolute}
.btn{position:absolute;background:var(--red);color:#fff;display:flex;align-items:center;justify-content:center;gap:14px;font-weight:500;font-size:18px}
.btn svg{width:14px;height:14px}
.photo{position:absolute;background:linear-gradient(160deg,var(--photo-mid),var(--photo-dark))}
.photo.light{background:linear-gradient(170deg,#8a8276 0%,#c9c2b4 45%,#ddd6c8 100%)}
.photo.patio{background:linear-gradient(180deg,#d9d9d6 0%,#8e4a3e 30%,#3d4042 55%,#2e3133 100%)}
.block{position:absolute;background:#555}

/* top bar & header */
.topbar{top:0;left:0;width:1200px;height:26px;background:var(--red);color:#fff;font-size:12px;font-weight:700;padding:5px 0 0 86px}
.topbar .socials{position:absolute;right:86px;top:6px;display:flex;gap:6px}
.topbar .socials span{width:12px;height:12px;border-radius:50%;border:1.5px solid #fff}
.header{top:26px;left:0;width:1200px;height:62px;background:var(--header-bg)}
.brand{left:86px;top:14px;font-weight:800;font-size:22px;color:var(--ink)}
.mail-info{right:160px;top:12px;text-align:right;font-size:15px;color:var(--ink)}
.mail-info b{font-size:15px}
.mail-icon{left:1055px;top:0;width:57px;height:62px;background:#fff;display:flex;align-items:center;justify-content:center}

/* hero */
.hero{top:124px;left:0;width:1200px;height:621px;background:linear-gradient(120deg,#6b4a3a 0%,#555 22%,#4a4a4a 55%,#5e5e5e 100%)}
.nav{top:88px;left:86px;width:1026px;height:74px;background:#fff;display:flex;justify-content:flex-end;align-items:center;padding-right:12px;font-size:16px;font-weight:600;color:var(--ink)}
.nav a{padding:0 18px;border-left:1.5px solid #333;line-height:20px}
.nav a:first-child{border:0}
.hero-title{right:573px;top:354px;text-align:right;color:#fff;font-weight:600;font-size:68px;line-height:75px}
.hero-sub{right:573px;top:574px;color:#fff;font-weight:700;font-size:26px}
.estimate{left:639px;top:213px;width:473px;height:477px;background:#fff;padding:40px 0 0 23px}
.estimate h2{font-size:30px;font-weight:600;color:var(--ink)}
.estimate p{font-size:15px;color:var(--ink);margin-top:4px}
.field{position:absolute;left:45px;width:356px;height:43px;background:var(--field);font-size:15px;color:#888;padding:12px 14px}
.field.select{background:#fff;border:1.5px solid #999}

/* about */
.about-lead{left:611px;top:845px;font-size:30px;font-weight:500;color:var(--ink)}
.about-title{left:611px;top:882px;font-size:40px;font-weight:700;color:var(--red)}
.about-copy{left:611px;top:958px;width:500px;font-size:16px;line-height:28.5px;text-align:justify;color:var(--ink)}
.stat{position:absolute;top:1132px;font-size:13px;font-weight:700;color:var(--ink);line-height:16px}
.stat svg{display:block;width:44px;height:46px;margin-bottom:16px}

/* services */
.services-bg{top:1465px;left:0;width:1200px;height:357px;background:var(--grey-bg)}
.services-title{left:86px;top:1510px;font-size:46px;font-weight:700;color:var(--ink)}
.services-copy{left:587px;top:1514px;width:530px;font-size:16px;line-height:28.5px;color:var(--ink)}
.card{position:absolute;top:1648px;width:325px;height:444px;background:#fff;box-shadow:0 0 6px rgba(0,0,0,.12);text-align:center}
.card .photo{left:0;top:0;width:325px;height:174px}
.card h3{position:absolute;top:212px;width:100%;font-size:16px;font-weight:700;color:var(--ink)}
.card p{position:absolute;top:258px;left:25px;width:275px;font-size:16px;line-height:26px;color:#444}
.card .btn{left:86px;top:371px;width:153px;height:47px}
.chev{top:1850px}

/* cta */
.cta{top:2189px;left:88px;width:1029px;height:188px;border:6px solid var(--red)}
.cta-brand{left:60px;top:50px;font-size:40px;font-weight:800;color:var(--ink);line-height:44px}
.cta-brand small{display:block;font-size:20px;color:var(--red);letter-spacing:2px;font-weight:700}
.cta-text{left:353px;top:48px;font-size:27px;font-weight:600;color:var(--ink);line-height:39px}

/* testimonials */
.section-title{left:0;width:1200px;text-align:center;font-size:49px;font-weight:700;color:var(--ink)}
.tcard{position:absolute;top:2560px;width:325px;height:208px;background:#f6f6f6}
.tcard .strip{position:absolute;left:0;top:0;width:43px;height:208px;background:#e6e6e6}
.tcard .avatar{position:absolute;left:7px;top:66px;width:78px;height:78px;border-radius:50%;background:linear-gradient(160deg,#6a5a3e,#2b2a28)}
.tcard .quote{position:absolute;left:97px;top:46px;width:222px;font-size:9.5px;line-height:20.5px;color:#222}
.tcard .name{position:absolute;left:97px;top:156px;font-size:16px;font-weight:700;color:var(--ink);line-height:17px}
.tcard .name small{display:block;font-size:8px;font-weight:500;line-height:10px}
.dot{top:2795px;width:38px;height:38px;border-radius:50%;background:var(--red);display:flex;align-items:center;justify-content:center}

/* gallery */
.gallery-copy{left:0;width:1200px;top:2998px;text-align:center;font-size:16px;line-height:29px;color:var(--ink)}
.gbtn{position:absolute;top:3404px;height:44px;color:#fff;font-size:19px;font-weight:500;display:flex;align-items:center;justify-content:center}

/* footer */
.footer{top:3685px;left:0;width:1200px;height:262px;background:var(--red);color:#fff}
.footer-logo{left:83px;top:34px;width:171px;height:187px;border:2px solid #fff;display:flex;align-items:center;justify-content:center;text-align:center;font-weight:700;font-size:22px;line-height:28px}
.fcol{position:absolute;top:38px;font-size:16px;line-height:28.5px}
.fcol h4{font-size:15px;font-weight:700;margin-bottom:2px}
.copyright{top:3947px;left:0;width:1200px;height:21px;background:#ededed;text-align:center;font-size:9px;padding-top:5px;color:#333}
</style>
</head>
<body>

<div class="abs topbar">BEST EPOXY RESIN FLOORING SERVICES COMPANY
  <div class="socials"><span></span><span></span><span></span><span></span></div>
</div>
<div class="abs header">
  <div class="abs brand">Venbrook Finishes</div>
  <div class="abs mail-info"><b>Send Us Email</b><br>info@example.com</div>
  <div class="abs mail-icon"><svg width="32" height="24" viewBox="0 0 32 24"><rect x="1" y="1" width="30" height="22" fill="none" stroke="#ec1c24" stroke-width="2"/><path d="M1 1l15 12L31 1M1 23l11-10M31 23L20 13" fill="none" stroke="#ec1c24" stroke-width="2"/></svg></div>
</div>

<div class="abs hero" role="img" aria-label="Photo of a grey tiled-effect epoxy patio floor beside timber stairs"></div>
<nav class="abs nav"><a>HOME</a><a>ABOUT US</a><a>OUR SERVICES</a><a>CONTACT US</a></nav>
<h1 class="abs hero-title">EPOXY<br>RESIN<br>FLOORING</h1>
<div class="abs hero-sub">Provide Quality Solutions</div>
<div class="btn" style="left:411px;top:648px;width:204px;height:40px;font-size:15px">VIEW OUR SERVICES <svg viewBox="0 0 14 14"><path d="M2 12L12 2M4 2h8v8" fill="none" stroke="#fff" stroke-width="1.5"/></svg></div>

<form class="abs estimate">
  <h2>Get a Free Estimate</h2>
  <p>Do you need our plumbing services? Contact us.</p>
  <div class="field" style="top:140px">Name</div>
  <div class="field" style="top:194px">Email</div>
  <div class="field" style="top:248px">Phone</div>
  <div class="field select" style="top:300px">Subject/Discuss about service
    <svg style="position:absolute;right:12px;top:16px" width="12" height="8" viewBox="0 0 12 8"><path d="M1 1l5 5 5-5" fill="none" stroke="#777" stroke-width="1.5"/></svg></div>
  <div class="btn" style="left:45px;top:368px;width:356px;height:43px;font-size:16px;justify-content:space-between;padding:0 14px">Submit Now <svg viewBox="0 0 14 14"><path d="M2 12L12 2M4 2h8v8" fill="none" stroke="#fff" stroke-width="1.5"/></svg></div>
</form>

<!-- about -->
<div class="photo light" style="left:86px;top:852px;width:210px;height:317px" role="img" aria-label="Photo of a speckled epoxy floor under a covered outdoor bar"></div>
<div class="block" style="left:317px;top:852px;width:210px;height:131px"></div>
<div class="photo light" style="left:317px;top:1003px;width:210px;height:317px" role="img" aria-label="Photo of a finished speckled epoxy patio with bar stools"></div>
<div class="block" style="left:86px;top:1189px;width:210px;height:131px"></div>

<div class="abs about-lead">Best Choice For Your</div>
<h2 class="abs about-title">EPOXY RESIN FLOORING</h2>
<p class="abs about-copy">Lorem ipsum dolor sit amet, consectetur adipisicing elit, sed do eiusmod tempor incididunt ut labore et dolore magna aliqua. Ut enim ad minim veniam, quis nostrud exercitation ullamco laboris nisi ut aliquip ex ea commod consequat. Duis aute irure dolor in reprehenderit in voluptate velit esse cillum.</p>

<div class="stat" style="left:611px;font-size:15px;line-height:19px"><svg viewBox="0 0 44 46"><rect x="2" y="4" width="38" height="38" fill="none" stroke="#ec1c24" stroke-width="2"/><path d="M2 18h38M2 30h38M15 4v38M28 4v38" stroke="#ec1c24" stroke-width="2"/></svg>3k+ Epoxy<br>Resin<br>Flooring<br>Done</div>
<div class="stat" style="left:755px"><svg viewBox="0 0 44 46"><path d="M6 40l14-14M20 26l16-20 4 4-20 16z" fill="none" stroke="#ec1c24" stroke-width="2"/><circle cx="6" cy="40" r="3" fill="none" stroke="#ec1c24" stroke-width="2"/></svg>3k+ Epoxy<br>Resin<br>Flooring<br>Done</div>
<div class="stat" style="left:896px"><svg viewBox="0 0 44 46"><rect x="4" y="8" width="36" height="30" rx="6" fill="none" stroke="#ec1c24" stroke-width="2"/><circle cx="12" cy="30" r="4" fill="none" stroke="#ec1c24" stroke-width="2"/><path d="M24 8v30" stroke="#ec1c24" stroke-width="2"/></svg>2k+<br>Consultations<br>Offered</div>
<div class="stat" style="left:1044px"><svg viewBox="0 0 44 46"><path d="M10 4h24v10H10zM16 14h12v8H16zM22 22v14M14 40h16" fill="none" stroke="#ec1c24" stroke-width="2"/></svg>2k+<br>Residents<br>Served</div>
<div class="btn" style="left:613px;top:1306px;width:153px;height:46px">Read More <svg viewBox="0 0 14 14"><path d="M2 12L12 2M4 2h8v8" fill="none" stroke="#fff" stroke-width="1.5"/></svg></div>

<!-- services -->
<div class="abs services-bg"></div>
<h2 class="abs services-title">Our services</h2>
<p class="abs services-copy">Lorem Ipsum is simply dummy text of the printing and typesetting industry. Lorem Ipsum has been the industry's standard dummy text ever since the 1500s.</p>

<svg class="abs chev" style="left:38px" width="18" height="30" viewBox="0 0 18 30"><path d="M15 2L3 15l12 13" fill="none" stroke="#222" stroke-width="2.5"/></svg>
<svg class="abs chev" style="left:1136px" width="18" height="30" viewBox="0 0 18 30"><path d="M3 2l12 13L3 28" fill="none" stroke="#222" stroke-width="2.5"/></svg>

<div class="card" style="left:88px"><div class="photo patio" role="img" aria-label="Photo of a dark tiled epoxy carport floor"></div><h3>Self-dispersing epoxy flooring</h3><p>Lorem Ipsum is simply dummy text of the printing and typesetting industry.</p><div class="btn">Learn More <svg viewBox="0 0 14 14"><path d="M2 12L12 2M4 2h8v8" fill="none" stroke="#fff" stroke-width="1.5"/></svg></div></div>
<div class="card" style="left:437px"><div class="photo patio" role="img" aria-label="Photo of a dark tiled epoxy carport floor"></div><h3>Self-Levelling Epoxy Flooring</h3><p>Lorem Ipsum is simply dummy text of the printing and typesetting industry.</p><div class="btn">Learn More <svg viewBox="0 0 14 14"><path d="M2 12L12 2M4 2h8v8" fill="none" stroke="#fff" stroke-width="1.5"/></svg></div></div>
<div class="card" style="left:787px"><div class="photo patio" role="img" aria-label="Photo of a dark tiled epoxy carport floor"></div><h3>Epoxy Vapour Barrier Flooring</h3><p>Lorem Ipsum is simply dummy text of the printing and typesetting industry.</p><div class="btn">Learn More <svg viewBox="0 0 14 14"><path d="M2 12L12 2M4 2h8v8" fill="none" stroke="#fff" stroke-width="1.5"/></svg></div></div>

<!-- call to action -->
<div class="abs cta">
  <div class="abs cta-brand">Venbrook<small>FINISHES</small></div>
  <div class="abs cta-text">Need Any Plubmber Services?<br>Call Us : +XXX-XXXXXXXXXX</div>
  <div class="btn" style="left:803px;top:57px;width:152px;height:48px">Learn More <svg viewBox="0 0 14 14"><path d="M2 12L12 2M4 2h8v8" fill="none" stroke="#fff" stroke-width="1.5"/></svg></div>
</div>

<!-- testimonials -->
<h2 class="abs section-title" style="top:2450px">Testimonial</h2>
<div class="tcard" style="left:86px"><div class="strip"></div><div class="avatar" role="img" aria-label="Customer portrait"></div><p class="quote">"Lorem Ipsum is simply dummy text of the printing and typesetting industry. Lorem Ipsum has been the industry's standard dummy text ever since the 1500s."</p><div class="name">Marla<small>Business women</small></div></div>
<div class="tcard" style="left:437px"><div class="strip"></div><div class="avatar" role="img" aria-label="Customer portrait"></div><p class="quote">"Lorem Ipsum is simply dummy text of the printing and typesetting industry. Lorem Ipsum has been the industry's standard dummy text ever since the 1500s."</p><div class="name">Marla<small>Business women</small></div></div>
<div class="tcard" style="left:787px"><div class="strip"></div><div class="avatar" role="img" aria-label="Customer portrait"></div><p class="quote">"Lorem Ipsum is simply dummy text of the printing and typesetting industry. Lorem Ipsum has been the industry's standard dummy text ever since the 1500s."</p><div class="name">Marla<small>Business women</small></div></div>
<div class="abs dot" style="left:557px"><svg width="10" height="16" viewBox="0 0 10 16"><path d="M8 2L2 8l6 6" fill="none" stroke="#fff" stroke-width="2"/></svg></div>
<div class="abs dot" style="left:604px"><svg width="10" height="16" viewBox="0 0 10 16"><path d="M2 2l6 6-6 6" fill="none" stroke="#fff" stroke-width="2"/></svg></div>

<!-- gallery -->
<h2 class="abs section-title" style="top:2910px">Gallery</h2>
<p class="abs gallery-copy">Incididunt ut labore et dolore magna aliqua quis nostrud exercitation ullamco laboris<br>nisi ut aliquip ex ea consequat duis aute irure dolor reprehenderit</p>
<div class="photo" style="left:86px;top:3079px;width:239px;height:296px;background:linear-gradient(180deg,#e8e8e6 0%,#d0d0ce 35%,#3e4143 55%,#2f3234 90%,#6b7a3c 100%)" role="img" aria-label="Photo of a dark speckled epoxy entry floor"></div>
<div class="photo patio" style="left:350px;top:3079px;width:237px;height:296px" role="img" aria-label="Photo of a tiled-effect epoxy carport"></div>
<div class="photo" style="left:612px;top:3079px;width:237px;height:296px;background:linear-gradient(180deg,#e4e4e2 0%,#cfcfcc 40%,#4a4d4f 60%,#6e7d3d 100%)" role="img" aria-label="Photo of a grey epoxy side path beside a garden"></div>
<div class="photo" style="left:875px;top:3079px;width:237px;height:296px;background:linear-gradient(180deg,#c6cbd2 0%,#aab0b8 30%,#3e4d62 55%,#2e3a4c 100%)" role="img" aria-label="Photo of a blue-grey tiled epoxy patio"></div>
<div class="gbtn" style="left:357px;width:141px;background:#555">LOAD MORE</div>
<div class="gbtn" style="left:510px;width:330px;background:var(--red)">VIEW MORE ON INSTAGRAM</div>

<!-- footer -->
<footer class="abs footer">
  <div class="abs footer-logo">Venbrook<br>Finishes</div>
  <div class="fcol" style="left:323px"><h4>QUICK LINKS</h4>Home<br>About us<br>Our services<br>Testimonial<br>Gallery</div>
  <div class="fcol" style="left:538px"><h4>GET IN TOUCH</h4>
    <div style="padding-left:28px;position:relative"><svg style="position:absolute;left:0;top:6px" width="16" height="22" viewBox="0 0 16 22"><path d="M8 21s7-8 7-13A7 7 0 001 8c0 5 7 13 7 13z" fill="none" stroke="#fff" stroke-width="2"/><circle cx="8" cy="8" r="2.5" fill="#fff"/></svg>XXX Lorem Ipsum<br>dummy tex - 75234</div>
    <div style="padding-left:28px;position:relative"><svg style="position:absolute;left:0;top:6px" width="18" height="18" viewBox="0 0 18 18"><path d="M4 1l3 4-2 2c1 3 3 5 6 6l2-2 4 3-2 3C7 17 1 11 1 3z" fill="#fff"/></svg>1 (555) 010-4477</div>
    <div style="padding-left:28px;position:relative;margin-top:28px"><svg style="position:absolute;left:0;top:8px" width="20" height="14" viewBox="0 0 20 14"><rect x="1" y="1" width="18" height="12" fill="none" stroke="#fff" stroke-width="1.5"/><path d="M1 1l9 7 9-7" fill="none" stroke="#fff" stroke-width="1.5"/></svg>info@example.com</div>
  </div>
  <div class="fcol" style="left:858px"><h4>FOLLOW US:</h4>
    <div style="display:flex;gap:6px;padding-left:14px;margin-top:4px"><span style="width:12px;height:12px;border-radius:50%;border:1.5px solid #fff"></span><span style="width:12px;height:12px;border-radius:50%;border:1.5px solid #fff"></span><span style="width:12px;height:12px;border-radius:50%;border:1.5px solid #fff"></span><span style="width:12px;height:12px;border-radius:50%;border:1.5px solid #fff"></span></div>
  </div>
</footer>
<div class="abs copyright">COPYRIGHT ©2024 ALL RIGHTS RESERVED.</div>

</body>
</html>
```